To revamp/upgrade company website

We recently changed our company core values and mission statement, I have added this (very simply) via word press. However I would like the values and mission statement page design upgrading and also to have them run through the rest of the website pages. Also, open to other recommendations on how to update our website. The main take away from the website should be that we are the "people company", both for our customers and our staff. We would like the logo and colour theme to remain as is. Calderwick Healthcare is a health and social care company, who privately own a group of care homes in the north west of england. Attached is the core values, PEOPLE, our mission statement and also a word cloud that we would also like to embed in to the website.

```html
<!DOCTYPE html>
<html lang="en">
<head>
<meta charset="utf-8">
<title>Our Refreshed Mission And Core Values – Calderwick Healthcare</title>
<link href="https://fonts.googleapis.com/css2?family=Playfair+Display:wght@900&family=Albert+Sans:wght@400;500;600&display=swap" rel="stylesheet">
<style>
:root{
  --navy:#1f3a5a;
  --orange:#e8895a;
  --text:#5d6470;
  --grey-bg:#f3f3f3;
  --white:#ffffff;
  --line:#e3e6ea;
}
*{margin:0;padding:0;box-sizing:border-box}
html,body{width:1200px;height:3238px;overflow:hidden}
body{position:relative;background:var(--white);font-family:"Albert Sans",Arial,sans-serif;color:var(--text)}
.abs{position:absolute}
.serif{font-family:"Playfair Display",Georgia,serif;font-weight:900;color:var(--navy)}
p{font-size:10.5px;line-height:15.5px}

/* header */
.site-header{left:0;top:0;width:1200px;height:75px}
.brand{left:83px;top:18px;display:flex;align-items:center;gap:10px}
.brand-mark{width:32px;height:32px;border-radius:50%;background:var(--navy)}
.brand-name{font-family:"Albert Sans",sans-serif;font-weight:600;font-size:28px;color:var(--navy);letter-spacing:.5px}
.nav-link{position:absolute;top:31px;font-size:10px;line-height:12px;color:var(--navy);white-space:nowrap}
.btn{background:var(--orange);color:var(--white);border-radius:16px;font-size:11px;font-weight:500;display:flex;align-items:center;justify-content:center}
.contact-btn{left:998px;top:23px;width:118px;height:30px}

/* hero */
.hero{left:0;top:75px;width:1200px;height:621px;border-radius:0 0 63px 63px;overflow:hidden;
  background:linear-gradient(90deg,#9a9a9a 0%,#b8b8b8 40%,#cfd3d6 65%,#e2e2e2 100%)}
.hero-title{left:83px;top:226px;font-size:68px;line-height:68px;color:var(--white)}
.hero-text{left:84px;top:442px;width:510px;color:var(--white);font-size:10px}
.scroll-down{left:576px;top:672px;width:48px;height:48px;border-radius:50%;background:var(--white);box-shadow:0 2px 10px rgba(0,0,0,.12);display:flex;align-items:center;justify-content:center}

/* sections */
.h2{font-size:35px;line-height:42px}
.center{text-align:center}
.photo{border-radius:14px}
.why-title{left:0;top:776px;width:1200px}
.why-intro{left:255px;top:829px;width:690px;text-align:center}
.why-photo{left:133px;top:902px;width:483px;height:261px;background:linear-gradient(135deg,#c9a99a,#e8e6e8 55%,#9fb9cf)}
.why-text{left:653px;top:930px;width:415px;font-size:10px}
.why-text p{font-size:10px}
.why-text p+p{margin-top:13px}

.believe-title{left:0;top:1232px;width:1200px}
.belief{top:1290px;width:190px;text-align:center}
.belief .icon{margin:0 auto 12px;width:72px;height:72px;border-radius:50%;display:flex;align-items:center;justify-content:center}
.bg-navy{background:var(--navy)}
.bg-orange{background:var(--orange)}

.mission-label{left:127px;top:1527px;color:var(--orange);font-size:12px}
.mission-title{left:127px;top:1550px}
.mission-text{left:127px;top:1642px;width:410px}
.visit-btn{left:127px;top:1728px;width:118px;height:29px}
.mission-photo{left:627px;top:1478px;width:445px;height:319px;background:linear-gradient(135deg,#5f7a3c,#c9ccd4 50%,#7a9450)}

.values{left:0;top:1880px;width:1200px;height:570px;background:linear-gradient(180deg,var(--grey-bg),#fafafa)}
.values-title{left:0;top:1934px;width:1200px}
.values-intro{left:330px;top:1989px;width:540px;text-align:center}
.value{width:340px;display:flex;align-items:center;gap:14px}
.value .icon{flex:none;width:72px;height:72px;border-radius:50%;background:var(--orange);display:flex;align-items:center;justify-content:center}
.value h3{font-size:17px;line-height:20px;margin-bottom:4px}
.value p{font-size:9.5px;line-height:14px}
.value.right{flex-direction:row-reverse;text-align:right}
.emblem{left:452px;top:2045px;width:296px;height:296px;border-radius:50%;background:var(--white);box-shadow:0 4px 18px rgba(0,0,0,.08);display:flex;align-items:center;justify-content:center}
.emblem-ring{position:absolute;inset:10px;border:2px dashed var(--orange);border-radius:50%}
.emblem-name{font-size:30px;font-weight:600;color:var(--navy)}
.values-outro{left:0;top:2380px;width:1200px;text-align:center}
.divider{left:83px;top:2453px;width:1034px;height:1px;background:var(--line)}

.next-photo{left:168px;top:2529px;width:414px;height:262px;background:linear-gradient(135deg,#d8d4d0,#eeeeee 50%,#b9acd6)}
.next-title{left:621px;top:2566px}
.next-text{left:621px;top:2624px;width:410px}
.next-text p{font-size:10px}
.next-text p+p{margin-top:8px}

/* footer */
.footer{left:0;top:2885px;width:1200px;height:353px;background:var(--navy);border-radius:75px 75px 0 0}
.footer-brand{left:132px;top:3040px;display:flex;align-items:center;gap:14px}
.footer-brand .brand-mark{background:var(--orange);width:44px;height:44px}
.footer-brand .brand-name{color:var(--white);font-size:40px}
.footer-h{font-size:24px;color:var(--white);line-height:30px;white-space:nowrap}
.loc-title{left:567px;top:2953px}
.loc-list{left:567px;top:2992px;list-style:none}
.loc-list li{display:flex;align-items:center;gap:10px;height:26.4px;font-size:10px;color:var(--white)}
.co-title{left:846px;top:2953px}
.co-credit{left:846px;top:2992px;font-size:10px;color:var(--white)}
.footer-line{left:83px;top:3189px;width:1034px;height:1px;background:rgba(255,255,255,.4)}
.copyright{left:0;top:3208px;width:1200px;text-align:center;font-size:10px;color:var(--white)}
.to-top{left:1137px;top:3170px;width:38px;height:38px;border-radius:50%;background:var(--orange);display:flex;align-items:center;justify-content:center}
</style>
</head>
<body>

<header class="abs site-header">
  <div class="abs brand"><span class="brand-mark"></span><span class="brand-name">Calderwick</span></div>
  <nav>
    <span class="nav-link" style="left:564px">About Us</span>
    <span class="nav-link" style="left:636px">Live With Us</span>
    <span class="nav-link" style="left:722px">How We Care</span>
    <span class="nav-link" style="left:813px">Help &amp; Support</span>
    <span class="nav-link" style="left:912px">Work With Us</span>
  </nav>
  <a class="abs btn contact-btn">Contact Us</a>
</header>

<section class="abs hero" role="img" aria-label="Photo of a carer tucking in a smiling elderly resident in a bright bedroom"></section>
<h1 class="abs serif hero-title">Our Refreshed<br>Mission And Core<br>Values</h1>
<p class="abs hero-text">We are pleased to share an important update that marks an exciting new chapter for our organisation. After thoughtful reflection, consultation, and feedback, we are proud to introduce our refreshed Company Values and Mission Statement – with a renewed commitment to placing people at the heart of everything we do.</p>
<div class="abs scroll-down"><svg width="16" height="16" viewBox="0 0 16 16" fill="none" stroke="#1f3a5a" stroke-width="1.5"><path d="M8 2v12M3 9l5 5 5-5"/></svg></div>

<h2 class="abs serif h2 center why-title">Why the Change?</h2>
<p class="abs why-intro">Over time, organisations evolve and so do the people who make them what they are. Earlier this year, we invited you to share the key values that you believe best represent how we work at Calderwick. These are reflected below and have proudly shaped the core values that define who we are as a Company.</p>
<div class="abs photo why-photo" role="img" aria-label="Photo of a carer talking with an elderly resident resting in bed"></div>
<div class="abs why-text">
  <p>We've listened carefully to your voices, looked at how we work and recognised the need to better articulate why we exist as an organisation and which values guide our work every day. This update is about more than words – it's about our identity, how we support one another, and how we deliver meaningful impact in a way that is truly aligned with our culture and aspirations.</p>
  <p>At the core of this change is a clear purpose: to become more people focu-sed. Within Calderwick, we provide life-changing support to our residents and their families. Together, we create a safe and caring environment for indivi-duals with rich histories and experiences. We recognise them as someone's mother, father, brother or sister; people who have cared for others in the past and helped shape the world we are privileged to live in today. During one of the most challenging times of their lives, our residents deserve no-thing less than to be cared for with dignity, compassion and respect.</p>
</div>

<h2 class="abs serif h2 center believe-title">We believe that:</h2>
<div class="abs belief" style="left:235px">
  <div class="icon bg-navy"><svg width="36" height="36" viewBox="0 0 36 36" fill="none" stroke="#fff" stroke-width="1.4"><circle cx="18" cy="18" r="12"/><path d="M18 24s-6-3.5-6-7.5a3 3 0 0 1 6-1 3 3 0 0 1 6 1c0 4-6 7.5-6 7.5z"/></svg></div>
  <p>Care is a relationship, not a transaction.</p>
</div>
<div class="abs belief" style="left:505px">
  <div class="icon bg-orange"><svg width="36" height="36" viewBox="0 0 36 36" fill="none" stroke="#fff" stroke-width="1.4"><circle cx="13" cy="10" r="3"/><circle cx="23" cy="10" r="3"/><path d="M8 18c0-3 2-5 5-5s5 2 5 5M18 18c0-3 2-5 5-5s5 2 5 5M5 24l8 5h10l8-7"/></svg></div>
  <p>Every resident deserves respect safety &amp; a true sense...</p>
</div>
<div class="abs belief" style="left:774px">
  <div class="icon bg-navy"><svg width="36" height="36" viewBox="0 0 36 36" fill="none" stroke="#fff" stroke-width="1.4"><circle cx="18" cy="11" r="4"/><path d="M10 28v-5a8 8 0 0 1 16 0v5M6 28h24"/></svg></div>
  <p>Every staff member deserves an environment...</p>
</div>

<span class="abs mission-label">Mission Statement</span>
<h2 class="abs serif h2 mission-title">Our New<br>Mission Statement</h2>
<p class="abs mission-text">"Our daily mission is to make each moment meaningful for us and for those around us through acts of kindness, integrity, and connection. We provide compassionate, person-centred care that honours the lives and legacies of our residents and their families, while fostering a culture where our staff feel empowered, valued, and inspired to grow."</p>
<a class="abs btn visit-btn">Book A Visit</a>
<div class="abs photo mission-photo" role="img" aria-label="Photo of an elderly couple laughing in a garden holding a basket of vegetables"></div>

<section class="abs values"></section>
<h2 class="abs serif h2 center values-title">Our Core Values</h2>
<p class="abs values-intro">We are introducing a new set of values that reflect our shared priorities and define how we show up for each other every day:</p>

<div class="abs value" style="left:109px;top:2057px">
  <div class="icon"><svg width="36" height="36" viewBox="0 0 36 36" fill="none" stroke="#fff" stroke-width="1.4"><circle cx="18" cy="13" r="6"/><path d="M6 18l6 10h12l6-10"/></svg></div>
  <div><h3 class="serif">Purpose</h3><p>We are driven by a clear understanding of why we do what we do to enrich lives, honour legacies...</p></div>
</div>
<div class="abs value" style="left:109px;top:2158px">
  <div class="icon"><svg width="36" height="36" viewBox="0 0 36 36" fill="none" stroke="#fff" stroke-width="1.4"><circle cx="18" cy="18" r="12"/><path d="M18 11l2 5h5l-4 3 1.5 5-4.5-3-4.5 3 1.5-5-4-3h5z"/></svg></div>
  <div><h3 class="serif">Excellence</h3><p>We hold ourselves the highest standards delivering exceptional care and creating...</p></div>
</div>
<div class="abs value" style="left:109px;top:2257px">
  <div class="icon"><svg width="36" height="36" viewBox="0 0 36 36" fill="none" stroke="#fff" stroke-width="1.4"><circle cx="18" cy="14" r="5"/><path d="M8 28c2-5 6-8 10-8s8 3 10 8M5 10l6 4M31 10l-6 4"/></svg></div>
  <div><h3 class="serif">Openness</h3><p>We build trust through honest respect communication welcoming feedback...</p></div>
</div>

<div class="abs value right" style="left:752px;top:2057px">
  <div class="icon"><svg width="36" height="36" viewBox="0 0 36 36" fill="none" stroke="#fff" stroke-width="1.4"><path d="M18 28s-9-5-9-11a5 5 0 0 1 9-3 5 5 0 0 1 9 3c0 6-9 11-9 11z"/></svg></div>
  <div><h3 class="serif">Passion</h3><p>We are passionate about delivering exceptional care. We take pride in what we do and in making...</p></div>
</div>
<div class="abs value right" style="left:752px;top:2158px">
  <div class="icon"><svg width="36" height="36" viewBox="0 0 36 36" fill="none" stroke="#fff" stroke-width="1.4"><path d="M6 12v15c4-2 8-2 12 0 4-2 8-2 12 0V12c-4-2-8-2-12 0-4-2-8-2-12 0zM18 12v15"/></svg></div>
  <div><h3 class="serif">Learning</h3><p>We are committed to personal and professional growth; empowering...</p></div>
</div>
<div class="abs value right" style="left:752px;top:2257px">
  <div class="icon"><svg width="36" height="36" viewBox="0 0 36 36" fill="none" stroke="#fff" stroke-width="1.4"><path d="M18 25s-6-3.5-6-7.5a3 3 0 0 1 6-1 3 3 0 0 1 6 1c0 4-6 7.5-6 7.5z"/><path d="M7 12a13 13 0 0 1 22 0M7 24a13 13 0 0 0 22 0"/></svg></div>
  <div><h3 class="serif">Empathy</h3><p>We actively listen and seek to understand before being understood, recognising the unique stories...</p></div>
</div>

<div class="abs emblem"><span class="emblem-ring"></span><span class="emblem-name">Calderwick</span></div>
<p class="abs values-outro">We believe these values shape the way we work together, make decisions, and deliver on our mission.</p>
<div class="abs divider"></div>

<div class="abs photo next-photo" role="img" aria-label="Photo of a carer holding hands with a smiling elderly man in bed"></div>
<h2 class="abs serif h2 next-title">What Happens Next?</h2>
<div class="abs next-text">
  <p>Over the coming weeks, we'll be embedding these values into how we work - from team conversations and recognition programmes to performance frameworks and leadership behaviours. We'll also be offering sessions where you can learn more about the mission and values, ask questions, and share your thoughts.</p>
  <p>We believe this shift will strengthen our culture, clarify our purpose, and create a more connected and supportive workplace.</p>
  <p>Thank you for everything you do, and for being part of this journey.</p>
</div>

<footer class="abs footer"></footer>
<div class="abs footer-brand"><span class="brand-mark"></span><span class="brand-name">Calderwick</span></div>
<h3 class="abs serif footer-h loc-title">Our Location</h3>
<ul class="abs loc-list">
  <li><svg width="10" height="10" viewBox="0 0 10 10"><path d="M2 1l2 2-1 1.5a6 6 0 0 0 2.5 2.5L7 6l2 2-1.5 1.5C4 9 1 6 .5 2.5z" fill="#e8895a"/></svg>Harrow Lea: 01632 960 410</li>
  <li><svg width="10" height="10" viewBox="0 0 10 10"><path d="M2 1l2 2-1 1.5a6 6 0 0 0 2.5 2.5L7 6l2 2-1.5 1.5C4 9 1 6 .5 2.5z" fill="#e8895a"/></svg>Elmstead Manor: 01632 960 522</li>
  <li><svg width="10" height="10" viewBox="0 0 10 10"><path d="M2 1l2 2-1 1.5a6 6 0 0 0 2.5 2.5L7 6l2 2-1.5 1.5C4 9 1 6 .5 2.5z" fill="#e8895a"/></svg>Corran House: 01632 960 138</li>
  <li><svg width="10" height="10" viewBox="0 0 10 10"><path d="M2 1l2 2-1 1.5a6 6 0 0 0 2.5 2.5L7 6l2 2-1.5 1.5C4 9 1 6 .5 2.5z" fill="#e8895a"/></svg>Linford Court: 01632 960 274</li>
  <li><svg width="10" height="10" viewBox="0 0 10 10"><path d="M2 1l2 2-1 1.5a6 6 0 0 0 2.5 2.5L7 6l2 2-1.5 1.5C4 9 1 6 .5 2.5z" fill="#e8895a"/></svg>Birch Meadow: 01632 960 391</li>
  <li><svg width="10" height="10" viewBox="0 0 10 10"><path d="M2 1l2 2-1 1.5a6 6 0 0 0 2.5 2.5L7 6l2 2-1.5 1.5C4 9 1 6 .5 2.5z" fill="#e8895a"/></svg>Old Quay Lodge: 01632 960 586</li>
</ul>
<h3 class="abs serif footer-h co-title">Calderwick Healthcare</h3>
<p class="abs co-credit">Website by Lanvale Media Group</p>
<div class="abs footer-line"></div>
<p class="abs copyright">©CopyRight 2025 Calderwick Healthcare. All rights reserved.</p>
<div class="abs to-top"><svg width="10" height="10" viewBox="0 0 10 10" fill="none" stroke="#fff" stroke-width="1.4"><path d="M2 6.5l3-3 3 3"/></svg></div>

</body>
</html>
```